シニア向け新商品(飲料)のLP制作をお願いします。

■制作数: 1ページ
■素材: 商品写真、文言はこちらで用意させていただきます。
■コーディング: 不要
■デザイン:PC版
■納品ファイル :イラストレーター形式 (.ai)
※完成後は当方でスマホ化を行うため、アウトラインなしもお願いします
■合計費用:5万円

※今回のデザインですが、別途添付しておりますラフ画(PowerPoint or PDF)の部分までお願いします。そのデザインにて恐縮ですが、選考をさせていただき、決定者様に3万円、また、ページの続き(下部の管理体制や価格についてのページデザインフィニッシュまで)は、同じ選考者様に+2万円にてお願いできればありがたく存じます。(選考決定の方への報酬は合計5万円になります。)

※パッケージ素材について
(PDF以外をご希望の場合は、相談して進めさせていただければと思います。 )

※テキストやキャッチコピーについては、そのままでもかまいませんし、
デザイン上、魅力的なものへリライト希望でしたら、添削等、自由とさせていただきます。

何卒よろしくお願い申し上げます。
ファイル添付が見られないというご指摘を受けたので、ファイルえを追加させていただきます。お手数ですがご参考いただければと存じます。
依頼金額を36000円に変更して、延長しました。
今回LP制作依頼が初めてであり、比較検討したく、もう少し様々なパターンな提案が欲しく延長させていただきました。
シニア層向けの若々しさが伝わるシンプルなデザインを希望します。
ラフ画像の指示が細かくて制作しにくい場合は多少削ってしまって全然問題ございませんので、ご検討していただければと思います。
また、不明点等がございましたら細かいことでもお申し付けください。
何卒よろしくお願いします。
期間を延長させていただきます。
皆様のご応募お待ちしております。

デザインがシンプルで今回のターゲット層にマッチしていたため。
また、修正や指摘に対しても柔軟かつ迅速に対応してくれて、制作をスピーディに進めていただいたことも大きかったです。

皆さま、この度はご提案ありがとうございます。
落選させていただい方につきましても、大変申し訳ございません。
またこのような機会を設けさせていただきたいので、その際は是非ともよろしくお願いいたします。

```html
<!DOCTYPE html>
<html lang="ja">
<head>
<meta charset="utf-8">
<title>あゆみ麦茶 | カラダ健康生活</title>
<link href="https://fonts.googleapis.com/css2?family=Noto+Sans+JP:wght@400;700;900&family=Noto+Serif+JP:wght@500;700;900&display=swap" rel="stylesheet">
<style>
:root{
  --green:#3f8a2e;
  --green-dark:#2d6b1f;
  --green-light:#e9f3dc;
  --red:#d2281c;
  --orange:#e3731e;
  --orange-pale:#fbe6d0;
  --gold:#c9a33a;
  --text:#333;
  --brown:#6b3b12;
  --white:#fff;
}
*{box-sizing:border-box;margin:0;padding:0}
html,body{width:1200px;height:5072px;overflow:hidden}
body{font-family:"Noto Sans JP",sans-serif;color:var(--text);background:#fff}
.canvas{width:1200px;height:5072px;position:relative;overflow:hidden}
.ph{display:block}

/* HERO */
.hero{position:relative;height:472px;background:linear-gradient(180deg,#f6e8c4 0%,#e8c785 45%,#c99a4c 100%);overflow:hidden}
.hero-bg{position:absolute;inset:0;background:linear-gradient(160deg,rgba(255,255,255,.35),rgba(200,150,70,.2) 60%,rgba(150,100,40,.35))}
.brand{position:absolute;left:16px;top:10px;background:var(--green);color:#fff;font-family:"Noto Serif JP",serif;font-weight:900;font-size:38px;padding:4px 26px;border-radius:6px;letter-spacing:2px}
.tagline{position:absolute;left:30px;top:70px;font-weight:700;font-size:19px;line-height:1.35;color:var(--green-dark);text-shadow:0 0 4px #fff}
.badges{position:absolute;left:16px;top:132px;width:380px;display:flex;flex-wrap:wrap;gap:10px 12px}
.badge{width:110px;height:110px;border-radius:50%;background:#fff;border:4px solid var(--green);display:flex;align-items:center;justify-content:center;text-align:center;font-weight:900;color:var(--green-dark);font-size:17px;line-height:1.25}
.badge.alt{background:var(--green);color:#fff;border-color:#fff}
.hero-note{position:absolute;left:16px;top:362px;font-size:12px;color:var(--brown);font-weight:700}
.tel{position:absolute;right:24px;top:8px;font-weight:900;color:var(--red);font-size:26px;display:flex;align-items:center;gap:6px;background:rgba(255,255,255,.85);padding:2px 12px;border-radius:4px}
.tel small{font-size:12px;color:var(--text)}
.info{position:absolute;top:56px;display:flex;gap:10px;right:24px}
.info-box{background:#fff;border:2px solid var(--green);border-radius:6px;padding:6px 12px;font-size:14px;font-weight:700;text-align:center;line-height:1.35;color:var(--green-dark)}
.info-box strong{color:var(--red)}
.product{position:absolute;left:660px;top:118px;width:360px;height:248px;border-radius:6px;background:linear-gradient(135deg,#fbf4e2,#e6cf98);box-shadow:0 6px 14px rgba(0,0,0,.25)}
.hotice{position:absolute;left:890px;top:300px;background:var(--red);color:#fff;width:110px;height:110px;border-radius:50%;display:flex;align-items:center;justify-content:center;text-align:center;font-weight:900;font-size:17px;line-height:1.3}
.pack{position:absolute;right:24px;top:320px;background:#fff;padding:6px 12px;border-radius:4px;font-size:14px;font-weight:700;text-align:center;line-height:1.35}
.cta-row{position:absolute;left:0;right:0;top:384px;display:flex;gap:18px;align-items:center;padding:0 16px}
.cta-limit{background:#fff;border:3px solid var(--red);color:var(--red);font-weight:900;font-size:16px;padding:4px 12px;line-height:1.3;border-radius:4px}
.cta-limit span{background:var(--red);color:#fff;padding:0 6px}
.cta-gift{background:linear-gradient(180deg,#e7c75e,var(--gold));color:#fff;font-weight:900;font-size:18px;padding:10px 28px;border-radius:40px;line-height:1.3;text-align:center;border:2px solid #fff}
.cta-btn{background:linear-gradient(180deg,#5aa83f,var(--green-dark));color:#fff;font-weight:900;font-size:20px;padding:14px 40px;border-radius:8px;box-shadow:0 3px 0 #1d4a12;display:flex;align-items:center;gap:10px}
.cta-btn svg{flex:none}

/* CONCERNS */
.concerns{position:relative;height:908px;background:#fff}
.sec-title{font-family:"Noto Serif JP",serif;font-weight:900;text-align:center}
.concerns .sec-title{position:absolute;left:0;right:0;top:36px;font-size:54px;color:#222;letter-spacing:3px}
.concerns .sec-title::after{content:"";display:block;width:640px;height:3px;background:var(--green);margin:10px auto 0}
.checklist{position:absolute;left:80px;top:170px;list-style:none;width:660px}
.checklist li{display:flex;align-items:center;gap:14px;font-size:28px;font-weight:700;margin-bottom:30px;line-height:1.35}
.checklist em{font-style:normal;color:var(--red);font-size:32px}
.check{width:36px;height:36px;flex:none}
.concern-photo{position:absolute;right:0;top:120px;width:460px;height:500px;background:linear-gradient(160deg,#eef0f2,#c9ced3 70%,#b5bcc4)}
.good-news{position:absolute;left:0;right:0;top:690px;text-align:center;font-size:34px;font-weight:900;color:var(--green-dark)}
.good-news::before,.good-news::after{content:"";display:inline-block;width:60px;height:2px;background:var(--green-dark);vertical-align:middle;margin:0 16px}
.change{position:absolute;left:170px;right:170px;top:760px;height:110px;border:3px solid var(--green);border-radius:10px;display:flex;align-items:center;justify-content:center;gap:8px;font-family:"Noto Serif JP",serif;font-weight:900;font-size:36px;color:var(--green-dark);background:var(--green-light)}
.change strong{font-size:50px;color:var(--orange)}

/* REASONS */
.reasons{position:relative;height:1860px;background:linear-gradient(180deg,#f8b978 0%,var(--orange-pale) 14%,#fdf3e8 60%,var(--orange-pale) 100%)}
.reasons .sec-title{padding-top:60px;font-size:48px;color:var(--brown);line-height:1.4}
.reasons .sec-title .big{display:inline-block;font-size:80px;color:var(--red);border-bottom:4px solid var(--red);padding:0 10px}
.reason-list{list-style:none;margin:40px 60px 0}
.reason{display:flex;gap:30px;margin-bottom:36px;align-items:flex-start}
.reason-body{flex:1}
.reason h3{display:flex;align-items:center;gap:14px;font-size:28px;font-weight:900;color:var(--brown);line-height:1.3;border-bottom:2px dotted var(--orange);padding-bottom:8px;margin-bottom:14px}
.reason h3 em{font-style:normal;color:var(--red)}
.num{width:54px;height:54px;border-radius:50%;background:var(--red);color:#fff;font-size:32px;display:flex;align-items:center;justify-content:center;flex:none}
.reason p{font-size:19px;line-height:1.7;padding-left:68px}
.reason-photo{width:300px;height:180px;margin-top:30px;border-radius:4px;flex:none}
.closing{text-align:center;font-family:"Noto Serif JP",serif;font-weight:900;color:var(--brown);font-size:44px;line-height:1.5;margin-top:30px}
.closing strong{font-size:64px;color:var(--red)}

/* COLUMN */
.column{position:relative;height:460px;background:#fff}
.column-head{position:absolute;left:60px;top:30px;display:flex;align-items:center}
.column-tag{background:var(--orange);color:#fff;font-family:"Noto Serif JP",serif;font-weight:900;font-size:36px;padding:6px 50px;border-radius:30px 0 0 30px;letter-spacing:8px}
.column-title{background:var(--orange-pale);color:var(--brown);font-weight:900;font-size:26px;padding:12px 30px;width:520px}
.column-text{position:absolute;left:60px;top:110px;width:700px;font-size:20px;line-height:1.7;border:2px solid var(--orange-pale);padding:18px 22px;background:#fffaf4}
.column-text em{font-style:normal;color:var(--red);font-weight:700}
.column-photo{position:absolute;right:40px;top:30px;width:340px;height:400px;background:linear-gradient(170deg,#f4f1ec,#d9d3c8)}

/* VOICES */
.voices{position:relative;height:1372px;background:linear-gradient(180deg,#dbecc8,var(--green-light) 30%,#eef5e6)}
.voices-head{position:relative;height:230px}
.bubble{position:absolute;background:#fff;border:3px solid var(--green);border-radius:50%;display:flex;align-items:center;justify-content:center;text-align:center;font-weight:700;font-size:15px;line-height:1.35;color:var(--green-dark)}
.voices-title{position:absolute;left:220px;width:680px;top:30px;background:#fff;border-radius:10px;text-align:center;padding:16px 0 20px;box-shadow:0 3px 0 var(--green)}
.voices-title .zoku{font-size:36px;font-weight:900;color:var(--red);letter-spacing:8px}
.voices-title h2{font-family:"Noto Serif JP",serif;font-weight:900;font-size:31px;color:var(--green-dark);margin-top:6px;white-space:nowrap}
.voice-list{list-style:none;margin:0 60px}
.voice{background:#fff;border-radius:8px;display:flex;gap:30px;padding:28px 36px;margin-bottom:34px;height:340px;box-shadow:0 2px 6px rgba(0,0,0,.1)}
.voice-body{flex:1}
.voice-name{font-size:18px;color:#666}
.voice h3{font-size:26px;font-weight:900;color:var(--green-dark);margin:6px 0 12px;border-bottom:2px dotted var(--green);padding-bottom:8px}
.voice p{font-size:19px;line-height:1.75}
.voice-photo{width:360px;height:280px;border-radius:4px;flex:none;background:linear-gradient(160deg,#e6e2db,#b9b2a6)}
</style>
</head>
<body>
<div class="canvas">

<header class="hero">
  <div class="hero-bg ph" role="img" aria-label="黄金色の麦畑の写真"></div>
  <div class="brand">あゆみ麦茶</div>
  <p class="tagline">ウォーキングや日常での<br>理想的な水分補給を応援！</p>
  <div class="badges">
    <div class="badge">ノン<br>カフェイン</div>
    <div class="badge">脂肪<br>ゼロ</div>
    <div class="badge">カロリー<br>ゼロ</div>
    <div class="badge alt">7つの<br>厳選素材</div>
    <div class="badge alt">アミノ酸<br>BCAA<br>配合</div>
  </div>
  <p class="hero-note">1日1杯からはじめる健康習慣</p>
  <div class="tel">
    <svg width="22" height="22" viewBox="0 0 24 24"><path fill="#d2281c" d="M6.6 10.8a15 15 0 006.6 6.6l2.2-2.2c.3-.3.7-.4 1-.2 1.1.4 2.3.6 3.6.6.6 0 1 .4 1 1V20c0 .6-.4 1-1 1A17 17 0 013 4c0-.6.4-1 1-1h3.5c.6 0 1 .4 1 1 0 1.3.2 2.5.6 3.6.1.3 0 .7-.2 1z"/></svg>
    <small>TEL</small>0120-246-810
  </div>
  <div class="info">
    <div class="info-box">ペットボトル1本分<br>(500ml)で<strong>33円</strong></div>
    <div class="info-box">国際食品品評会<br>最高金賞受賞スタッフが開発</div>
  </div>
  <div class="product ph" role="img" aria-label="あゆみ麦茶の商品パッケージ写真"></div>
  <div class="hotice">ホットでも！<br>アイスでも！</div>
  <div class="pack">1袋4g×30包入り<br>(日本製)</div>
  <div class="cta-row">
    <div class="cta-limit">今だけ限定！<br>健康習慣のチャンス！<br><span>プレゼント実施中！</span></div>
    <div class="cta-gift">1リットル分の<br>無料サンプル</div>
    <a class="cta-btn">
      <svg width="22" height="22" viewBox="0 0 24 24"><path fill="#fff" d="M9 5l7 7-7 7z"/></svg>無料サンプルはこちら</a>
    <a class="cta-btn">
      <svg width="22" height="22" viewBox="0 0 24 24"><path fill="#fff" d="M9 5l7 7-7 7z"/></svg>お申し込みはこちら</a>
  </div>
</header>

<section class="concerns">
  <h2 class="sec-title">こんなお悩みありませんか？</h2>
  <ul class="checklist">
    <li><svg class="check" viewBox="0 0 36 36"><rect x="2" y="6" width="26" height="26" fill="#fff" stroke="#888" stroke-width="2"/><path d="M8 18l7 8L33 4" fill="none" stroke="#d2281c" stroke-width="5"/></svg><span>最近、<em>運動不足</em>気味かも…</span></li>
    <li><svg class="check" viewBox="0 0 36 36"><rect x="2" y="6" width="26" height="26" fill="#fff" stroke="#888" stroke-width="2"/><path d="M8 18l7 8L33 4" fill="none" stroke="#d2281c" stroke-width="5"/></svg><span>ウォーキングの時って<em>何を飲めば</em>いいのだろう？</span></li>
    <li><svg class="check" viewBox="0 0 36 36"><rect x="2" y="6" width="26" height="26" fill="#fff" stroke="#888" stroke-width="2"/><path d="M8 18l7 8L33 4" fill="none" stroke="#d2281c" stroke-width="5"/></svg><span>この先もずっと<em>アクティブ</em>でいたい！</span></li>
    <li><svg class="check" viewBox="0 0 36 36"><rect x="2" y="6" width="26" height="26" fill="#fff" stroke="#888" stroke-width="2"/><path d="M8 18l7 8L33 4" fill="none" stroke="#d2281c" stroke-width="5"/></svg><span>運動時も日常も飲める<em>カラダに優しい</em><br><em>健康的な飲み物</em>が欲しい！</span></li>
    <li><svg class="check" viewBox="0 0 36 36"><rect x="2" y="6" width="26" height="26" fill="#fff" stroke="#888" stroke-width="2"/><path d="M8 18l7 8L33 4" fill="none" stroke="#d2281c" stroke-width="5"/></svg><span>将来のために美味しく続けられる<br><em>「ラクラク健康習慣」</em>を手に入れたい！</span></li>
  </ul>
  <div class="concern-photo ph" role="img" aria-label="肩に手を当てる年配の男性の写真"></div>
  <p class="good-news">そんなあなたに朗報！</p>
  <div class="change">あゆみ麦茶で変わる<strong>『カラダ健康生活！』</strong></div>
</section>

<section class="reasons">
  <h2 class="sec-title">あゆみ麦茶が選ばれる<br><span class="big">「5つ」</span>の理由！</h2>
  <ol class="reason-list">
    <li class="reason">
      <div class="reason-body">
        <h3><span class="num">1</span><span>7つの厳選成分を<em>「運動する大人」</em>のために贅沢ブレンド！</span></h3>
        <p>健康を考える大人に大人気、選び抜かれた7つの厳選原料（大麦、玄米、はとむぎ、羅布麻、チコリ、黒大豆、キヌア）が、運動時はもちろん、毎日の理想的な水分補給をしっかりサポートします！</p>
      </div>
      <div class="reason-photo ph" role="img" aria-label="厳選された穀物原料の写真" style="background:linear-gradient(135deg,#e9d6b3,#b98f5a)"></div>
    </li>
    <li class="reason">
      <div class="reason-body">
        <h3><span class="num">2</span><span>運動時や日常生活で大切な<em>「必須アミノ酸」「チロシン」</em>も配合！</span></h3>
        <p>「BCAA」をはじめとする「複数のアミノ酸」「チロシン」も配合！これらは体内で合成されないため、食事などの外部からの摂取が必要になります。</p>
      </div>
      <div class="reason-photo ph" role="img" aria-label="ウォーキングする年配の夫婦の写真" style="background:linear-gradient(135deg,#dfe9c9,#8fae6a)"></div>
    </li>
    <li class="reason">
      <div class="reason-body">
        <h3><span class="num">3</span><span>嬉しい糖質＆脂肪ゼロ＆ノンカフェイン！</span></h3>
        <p>お子様ももちろん、全世代で安心してご愛飲いただけます。さらにうれしいノンカフェイン。※カフェインには利尿作用も多く、水分が体外に出ていく原因にもなってしまいます。</p>
      </div>
      <div class="reason-photo ph" role="img" aria-label="グラスに注がれた麦茶の写真" style="background:linear-gradient(135deg,#f3e2c4,#b86f25)"></div>
    </li>
    <li class="reason">
      <div class="reason-body">
        <h3><span class="num">4</span><span>どんな食事にも合う、香ばしく豊かな味わい！</span></h3>
        <p>毎日飲んでも飽きの来ない麦茶ベースに、様々な厳選穀物の豊かな味わい。運動時はもちろん、どんな食事ともベストマッチします。ご家庭の食卓にもぜひご活用ください。</p>
      </div>
      <div class="reason-photo ph" role="img" aria-label="和食の食卓の写真" style="background:linear-gradient(135deg,#e8d2b0,#9b6a3a)"></div>
    </li>
    <li class="reason">
      <div class="reason-body">
        <h3><span class="num">5</span><span>確かな品質管理体制（放射能検査・残留農薬検査も実施）</span></h3>
        <p>栄養のプロである管理栄養士、運動のプロである専門トレーナー、最高金賞受賞のスタッフが共同開発。お客様の元に届くまで、製造ロットごとにきめ細かい厳重な品質管理を行っています。</p>
      </div>
      <div class="reason-photo ph" role="img" aria-label="品質検査を行う研究室の写真" style="background:linear-gradient(135deg,#eef1f4,#a9b6c2)"></div>
    </li>
  </ol>
  <p class="closing">だから<strong>「あゆみ麦茶」</strong><br>は多くの方に選ばれています。</p>
</section>

<section class="column">
  <div class="column-head">
    <span class="column-tag">コラム</span>
    <span class="column-title">水分補給の大切さとあゆみ麦茶</span>
  </div>
  <p class="column-text">体の７０％を占める水分。それだけ体にとって水分とは大切な存在。毎日の水分補給の質を改善することをオススメいたします。何となく日頃の水分補給がうまく取り組めない、運動時にキレが悪いなど、多くの場合体のコンディションが悪いことが原因である場合があります。そこで、水分補給の質にこだわりたい方のために「<em>あゆみ麦茶</em>」は生まれました。ホルモンなどを中心に、毎日のリセットを目指します。さらにコクのある味わいも、是非お楽しみください。</p>
  <div class="column-photo ph" role="img" aria-label="資料を持つ女性スタッフの写真"></div>
</section>

<section class="voices">
  <div class="voices-head">
    <div class="bubble" style="left:40px;top:30px;width:150px;height:130px">ウォーキングに<br>いつも<br>持っています！</div>
    <div class="bubble" style="left:920px;top:20px;width:130px;height:120px">ジムの仲間と<br>一緒に<br>飲んでいます♪</div>
    <div class="bubble" style="left:1056px;top:80px;width:136px;height:130px">いつもハツラツ！<br>みんなに<br>配っています</div>
    <div class="voices-title">
      <p class="zoku">ぞくぞく！</p>
      <h2>全国からご利用者さまの声が届いています！</h2>
    </div>
  </div>
  <ul class="voice-list">
    <li class="voice">
      <div class="voice-body">
        <p class="voice-name">岡山県・花江さま（55歳）</p>
        <h3>心も体も健康に。夫婦で毎日飲んでいます！</h3>
        <p>日々の健康にはやっぱりずっと気になりました。毎日ジョギングと共に飲むようになって、体がとても軽くなった気がします。夫婦で散歩しながら楽しく続けています。これからも、生活を楽しみながら続けたいと思います。</p>
      </div>
      <div class="voice-photo ph" role="img" aria-label="利用者の女性の写真"></div>
    </li>
    <li class="voice">
      <div class="voice-body">
        <p class="voice-name">岡山県・花江さま（55歳）</p>
        <h3>心も体も健康に。夫婦で毎日飲んでいます！</h3>
        <p>日々の健康にはやっぱりずっと気になりました。毎日ジョギングと共に飲むようになって、体がとても軽くなった気がします。夫婦で散歩しながら楽しく続けています。これからも、生活を楽しみながら続けたいと思います。</p>
      </div>
      <div class="voice-photo ph" role="img" aria-label="利用者の夫婦の写真"></div>
    </li>
    <li class="voice">
      <div class="voice-body">
        <p class="voice-name">岡山県・花江さま（55歳）</p>
        <h3>心も体も健康に。夫婦で毎日飲んでいます！</h3>
        <p>日々の健康にはやっぱりずっと気になりました。毎日ジョギングと共に飲むようになって、体がとても軽くなった気がします。夫婦で散歩しながら楽しく続けています。これからも、生活を楽しみながら続けたいと思います。</p>
      </div>
      <div class="voice-photo ph" role="img" aria-label="ウォーキングする利用者の写真"></div>
    </li>
  </ul>
</section>

</div>
</body>
</html>
```